VELINTA Promotions - Business Card Design Project

We are looking for a classy business cards for Promotion Company based in Toronto, Canada named Velinta Promotions.

Velinta Promotions has an idea and vision to set high standard, be EXCLUSIVE and attract a group of people that will follow us through events we promote (night clubs, brand promotions, music events, and sport events)

We want to present a high standards and classy image to the others...
Updates

Target Market(s)

male/female age 25-40 Target: business owners young entrepreneur - clubing industry - media industry - promotion industry - marketing media industry

Industry/Entity Type

Events

Requirements
Must have
• business cards should be classy, make people feel exclusive , make people react ..

```html
<!DOCTYPE html>
<html lang="en">
<head>
<meta charset="utf-8">
<title>Velinta Promotions – Business Cards</title>
<link rel="stylesheet" href="https://fonts.googleapis.com/css2?family=Cinzel:wght@400;600&family=Questrial&display=swap">
<style>
  :root {
    --page-bg: #ebe8e4;
    --brand-blue: #00b4ec;
    --card-white: #ffffff;
    --photo-dark: #1c1c1c;
    --photo-mid: #6a6a6a;
    --photo-light: #b9b9b9;
    --card-shadow: rgba(0, 0, 0, 0.28);
  }
  * { margin: 0; padding: 0; box-sizing: border-box; }
  html, body { width: 1200px; height: 1139px; overflow: hidden; }
  body { background: var(--page-bg); position: relative; }

  .card {
    position: absolute;
    width: 752px;
    height: 429px;
    overflow: hidden;
    box-shadow: 0 6px 18px var(--card-shadow);
  }

  /* Front */
  .card--front { left: 70px; top: 53px; }
  .skyline-photo {
    position: absolute;
    inset: 0;
    background:
      linear-gradient(180deg,
        var(--photo-light) 0%,
        var(--photo-mid) 28%,
        #8e8e8e 42%,
        var(--photo-dark) 52%,
        #2a2a2a 62%,
        var(--photo-mid) 78%,
        #9a9a9a 100%);
  }
  .front-brand {
    position: absolute;
    left: 52px;
    top: 296px;
    color: var(--brand-blue);
    font-family: "Cinzel", serif;
    font-weight: 600;
  }
  .front-brand .brand-name {
    display: block;
    font-size: 82px;
    line-height: 1;
    letter-spacing: 2px;
  }
  .front-brand .brand-tagline {
    display: block;
    margin-top: 8px;
    margin-left: 312px;
    font-size: 21px;
    letter-spacing: 6px;
    color: var(--card-white);
  }

  /* Back */
  .card--back { left: 387px; top: 553px; background: var(--brand-blue); }
  .back-brand {
    position: absolute;
    right: 62px;
    top: 46px;
    color: var(--card-white);
    font-family: "Cinzel", serif;
    font-weight: 600;
    text-align: right;
  }
  .back-brand .brand-name {
    display: block;
    font-size: 40px;
    line-height: 1;
    letter-spacing: 1px;
  }
  .back-brand .brand-tagline {
    display: block;
    margin-top: 2px;
    font-size: 11px;
    letter-spacing: 4px;
  }
  .contact-row {
    position: absolute;
    left: 34px;
    bottom: 64px;
    display: flex;
    gap: 42px;
    color: var(--card-white);
    font-family: "Questrial", sans-serif;
    font-size: 18px;
    list-style: none;
  }
</style>
</head>
<body>
  <section class="card card--front" aria-label="Business card front">
    <div class="skyline-photo" role="img" aria-label="Black and white photograph of a city skyline at dusk reflected in water, with a white floral flourish"></div>
    <div class="front-brand">
      <span class="brand-name">VELINTA</span>
      <span class="brand-tagline">PROMOTIONS</span>
    </div>
  </section>

  <section class="card card--back" aria-label="Business card back">
    <div class="back-brand">
      <span class="brand-name">VELINTA</span>
      <span class="brand-tagline">PROMOTIONS</span>
    </div>
    <ul class="contact-row">
      <li class="contact-email">name@velinta.com</li>
      <li class="contact-address">1 street, town, code</li>
      <li class="contact-phone">+27 82 55 01 234</li>
    </ul>
  </section>
</body>
</html>
```